Infographic - Iceberg Strategy Process

We need to develop a simple infographic that shows our process for running a team corporate strategy day. the aim is to simply outline the steps and show that most of the work happens well before a team meets for the company's 'off-site' or strategy day (the work that happens below the waterline). See our website for style reference morrowplk.example

We are team strategy facilitators. We facilitate corporate team strategy days that usually run for 1 or 2 days.

We call our process a collaborative strategy process, because we seeking input and contribution from our clients staff, customers and clients in the weeks ahead of the actual facilitated strategy day.

We believe this is the best way to develop a winning strategy is to talk, engage and generate insight from the people you deliver value to.

Most companies (and teams) think that running a successful team strategy day (or workshop) is about getting their team into a room for the workshop and brainstorming ideas.
It's not. In fact the workshop happens toward the process and there are some key steps that need to happen well before the team ever gets into the room - this is what we are trying to portray in the infographic.

We describe the process as being like an iceberg - meaning that the team strategy day (workshop) is really only the the 'tip of the iceberg' and most of the work is done by talking to leaders, staff and clients well before the teams gets together in a room for the strategy day workshop. The pre-workshop steps are often or never undertaken.

We describe the steps before the workshop as being like that part of an iceberg that's 'below the water' because they're the necessary steps that the workshop attendees never see but they makes up the majority of the work (Only 1/10th of an iceberg is above the water http://en.lorebank.example/wiki/Iceberg - See and read the overview section)

Corin

https://slides.vantory.example/presentation/d/7mTkwqobnuvE3-K9sLfGhPzXaRcYdNwBjmVtlQe2xy4/pub?start=false&loop=false&delayms=60000

Target Market(s)

Businesses and corporate teams in business, finance and professional services

Industry/Entity Type

Call

Font styles to use
Sans Serif

Requirements
Must have
• Morrow PLK Logo
• Morrow PLK website reference
• clean, clear design, alignment with Logo colours (logo .png attached)
• Alignment with design of our website style - clean and corporate. We use Google fonts like Raleway (for headings), Merriweather (for content) in our documents

```html
<!DOCTYPE html>
<html lang="en">
<head>
<meta charset="utf-8">
<title>Collaborative Strategy – The Iceberg Process</title>
<link rel="stylesheet" href="https://fonts.googleapis.com/css2?family=Raleway:wght@400;500;600;700;800&family=Merriweather:wght@400;700&display=swap">
<style>
  :root {
    --ocean: #2f7db8;
    --ocean-deep: #266fa8;
    --header-band: #17578f;
    --ink: #1e2a33;
    --white: #ffffff;
    --row-1: #f6f7f9;
    --row-2: #dfe4e8;
    --row-3: #c6def0;
    --row-4: #9dccec;
    --row-5: #7bbbe8;
    --row-6: #5caae3;
    --tier-1: #f3f5f7;
    --tier-2: #e2e6ea;
    --tier-3: #c9e3f4;
    --tier-4: #a6d5f2;
    --tier-5: #71bdeb;
    --tier-6: #4ea9e4;
    --arrow: #2a6fc4;
    --waterline: #1c5b9e;
    --footer: #d7d7d8;
    --brand: #3b3d40;
    --link: #1f63b0;
  }
  * { margin: 0; padding: 0; box-sizing: border-box; }
  html, body { width: 1200px; height: 748px; overflow: hidden; }
  body { background: var(--ocean); font-family: "Raleway", sans-serif; }

  .infographic {
    position: relative;
    width: 1200px;
    height: 748px;
    overflow: hidden;
    background: radial-gradient(ellipse at 45% 40%, var(--ocean) 0%, var(--ocean-deep) 100%);
  }

  .shapes { position: absolute; inset: 0; }

  .title {
    position: absolute;
    left: 32px; top: 19px;
    color: var(--white);
    font-size: 21px;
    font-weight: 500;
    letter-spacing: 0.6px;
    text-transform: uppercase;
  }

  .timeline { list-style: none; }
  .timeline li {
    position: absolute;
    left: 38px;
    color: var(--white);
    font-size: 16px;
    font-weight: 500;
  }
  .timeline .timeline-heading {
    font-size: 15px;
    font-weight: 700;
    letter-spacing: 0.4px;
    text-transform: uppercase;
  }

  .tier-label {
    position: absolute;
    width: 240px;
    text-align: center;
    color: var(--ink);
    font-size: 15px;
    font-weight: 600;
    line-height: 17px;
    transform: translateX(-50%);
  }
  .tier-label.is-feature { font-size: 21px; font-weight: 700; }

  .step-detail {
    position: absolute;
    color: var(--ink);
    font-family: "Merriweather", serif;
    white-space: nowrap;
  }
  .step-detail p { margin: 0; }
  .step-detail.size-l { font-size: 11.5px; line-height: 14.5px; }
  .step-detail.size-m { font-size: 11px; line-height: 12.2px; }
  .step-detail.size-s { font-size: 10px; line-height: 11.6px; }

  .footer {
    position: absolute;
    left: 0; top: 632px;
    width: 1200px; height: 116px;
    background: linear-gradient(180deg, #dcdcdd 0%, var(--footer) 100%);
  }
  .brand-name {
    position: absolute;
    left: 38px; top: 10px;
    font-size: 37px;
    font-weight: 800;
    letter-spacing: 0.5px;
    color: var(--brand);
    text-transform: uppercase;
  }
  .brand-tagline {
    position: absolute;
    left: 40px; top: 61px;
    font-family: "Merriweather", serif;
    font-size: 16px;
    color: #333638;
  }
  .brand-site {
    position: absolute;
    left: 40px; top: 82px;
    font-family: "Merriweather", serif;
    font-size: 14px;
    font-weight: 700;
    color: var(--link);
    text-decoration: none;
  }
</style>
</head>
<body>
<main class="infographic">

  <svg class="shapes" width="1200" height="748" viewBox="0 0 1200 748" aria-hidden="true">
    <defs>
      <marker id="arrow-head" viewBox="0 0 10 10" refX="9" refY="5" markerWidth="10" markerHeight="10" markerUnits="userSpaceOnUse" orient="auto">
        <path d="M0 0 L10 5 L0 10 Z" fill="var(--arrow)"/>
      </marker>
    </defs>

    <!-- header band -->
    <polygon points="0,0 642,0 612,66 0,66" fill="var(--header-band)"/>

    <!-- detail rows -->
    <g class="detail-rows">
      <polygon points="462,77 1163,77 1163,187 521,187" fill="var(--row-1)"/>
      <polygon points="521,187 1163,187 1163,268 565,268" fill="var(--row-2)"/>
      <polygon points="565,268 1163,268 1163,357 613,357" fill="var(--row-3)"/>
      <polygon points="613,357 1163,357 1163,445 660,445" fill="var(--row-4)"/>
      <polygon points="660,445 1163,445 1163,525 703,525" fill="var(--row-5)"/>
      <polygon points="703,525 1163,525 1163,603 745,603" fill="var(--row-6)"/>
      <polygon points="462,77 612,77 890,603 745,603" fill="#ffffff" opacity="0.14"/>
    </g>

    <!-- pyramid tiers -->
    <g class="iceberg">
      <polygon points="462,75 522,187 405,187" fill="var(--tier-1)"/>
      <polygon points="405,187 522,187 574,285 355,285" fill="var(--tier-2)"/>
      <polygon points="355,285 574,285 623,375 309,375" fill="var(--tier-3)"/>
      <polygon points="309,375 623,375 670,463 264,463" fill="var(--tier-4)"/>
      <polygon points="264,463 670,463 714,545 222,545" fill="var(--tier-5)"/>
      <polygon points="222,545 714,545 752,617 185,617" fill="var(--tier-6)"/>
      <g stroke="#ffffff" stroke-opacity="0.55" stroke-width="1.5">
        <line x1="405" y1="187" x2="522" y2="187"/>
        <line x1="355" y1="285" x2="574" y2="285"/>
        <line x1="264" y1="463" x2="670" y2="463"/>
        <line x1="222" y1="545" x2="714" y2="545"/>
      </g>
      <path class="waterline" d="M306 375 q6 -5 12 0 t12 0 t12 0 t12 0 t12 0 t12 0 t12 0 t12 0 t12 0 t12 0 t12 0 t12 0 t12 0 t12 0 t12 0 t12 0 t12 0 t12 0 t12 0 t12 0 t12 0 t12 0 t12 0 t12 0 t12 0 t12 0"
            fill="none" stroke="var(--waterline)" stroke-width="2"/>
    </g>

    <!-- connectors -->
    <g class="connectors" stroke="var(--arrow)" stroke-width="1.6" stroke-dasharray="4 3" marker-end="url(#arrow-head)">
      <line x1="535" y1="138" x2="620" y2="138"/>
      <line x1="570" y1="228" x2="655" y2="228"/>
      <line x1="620" y1="313" x2="705" y2="313"/>
      <line x1="662" y1="400" x2="747" y2="400"/>
      <line x1="708" y1="485" x2="791" y2="485"/>
      <line x1="750" y1="566" x2="833" y2="566"/>
    </g>
  </svg>

  <h1 class="title">Collaborative Strategy &nbsp;- The Iceberg Process</h1>

  <ol class="timeline">
    <li class="timeline-heading" style="top:82px">Weeks after Worship</li>
    <li style="top:148px">2 Weeks after Workshop</li>
    <li style="top:231px">1 Week after Workshop</li>
    <li style="top:319px">Workshop Week</li>
    <li style="top:405px">1 Week to go</li>
    <li style="top:498px">2 Weeks to go</li>
    <li style="top:564px">3 Weeks to go</li>
  </ol>

  <div class="tier-label" style="left:462px; top:167px">Communicate<br>&amp; Feedback</div>
  <div class="tier-label" style="left:463px; top:226px">Strategy on Page<br>(Strategy Map)</div>
  <div class="tier-label is-feature" style="left:464px; top:320px">Team Strategy Day</div>
  <div class="tier-label" style="left:464px; top:411px">Customer and Staff Insight</div>
  <div class="tier-label" style="left:464px; top:497px">Secondary (Desk) Research</div>
  <div class="tier-label" style="left:464px; top:573px">Kickoff and Scoping</div>

  <div class="step-detail size-l" style="left:650px; top:96px">
    <p>Seek Feedback &amp; Communication</p>
    <p>Communicate to the workshop group &amp; seek feedback.</p>
    <p>Incorporate feedback into strategy document and tweak where needed.</p>
    <p>Coach the team to be your ‘market strategy evangelists’ to communicate the</p>
    <p>strategy throughout the organisation.</p>
  </div>

  <div class="step-detail size-l" style="left:679px; top:191px">
    <p>Create Strategy Map &amp; Strategy Summary</p>
    <p>Create a strategy map on one page</p>
    <p>Create a Strategy Summary Deck in SlideForge (10-12 slides)</p>
    <p>Create an action plan and responsibility pages for pricing, services, target</p>
    <p>market and promotion strategies</p>
  </div>

  <div class="step-detail size-m" style="left:732px; top:270px">
    <p>Team Strategy Workshop</p>
    <p>Define or review the purpose - ‘the reason your company exists’</p>
    <p>1 Blue Sky - create/define your ideal future</p>
    <p>2 Objective &amp; Goals - define your goals &amp; objectives</p>
    <p>3 Positioning - define market positioning vs competitors and alternatives</p>
    <p>4 Critical Issues - define critical issues for success</p>
    <p>5 Roadmap - create a 12 month roadmap to meet objectives</p>
  </div>

  <div class="step-detail size-m" style="left:768px; top:359px">
    <p>Generate Insight</p>
    <p>Generate insight on your company, customer and competitors via:</p>
    <p>1 customer surveys &amp; conversations</p>
    <p>2 staff surveys &amp; conversations</p>
    <p>3 workshop attendee interviews</p>
    <p>Ask for ideas on “how do you win?”, “what should you be doing?” and “if</p>
    <p>you were running things, what would you do?”</p>
  </div>

  <div class="step-detail size-s" style="left:812px; top:449px">
    <p>Scan the Environment and Hypothesise</p>
    <p>Internal Scan - review past strategy documents, marketing plans,</p>
    <p>website.</p>
    <p>External Scan - assess competitors and alternatives. Look at the impact</p>
    <p>technology has on decision making.</p>
    <p>Develop Hypothesis - develop your marketing strategy hypothesis for</p>
    <p>testing.</p>
  </div>

  <div class="step-detail size-s" style="left:858px; top:530px">
    <p>Define the Purpose of the Workshop.</p>
    <p>Meet with leaders, senior management and key</p>
    <p>stakeholders.</p>
    <p>Define what a successful strategy day will look like.</p>
    <p>Look for clashes and common ground and create a brief.</p>
    <p>Finally, make a list of workshop participants.</p>
  </div>

  <footer class="footer">
    <div class="brand-name">Morrow PLK</div>
    <p class="brand-tagline">Marketing Strategy - Facilitators Advisors &amp; Consultants</p>
    <a class="brand-site" href="http://www.morrowplk.example">www.morrowplk.example</a>
  </footer>

</main>
</body>
</html>
```